Design some Business Cards for Consultant

Most of my work is in financial & analytical consulting for microfinance and low-income housing finance, mainly in developing countries (Asia, Africa, Latin America). You can see samples of my published work here: tobiaswenkle.com (main page is the blog; navigate to /papers for other published work).

Looking for a clean, no-nonsense design with limited text (name, city, website, email, skype & phone). Single-sided. Would like to print on recycled paper stock, so consider this in the design. If you can work with a (reasonably priced) online printer that ships to Belgium at reasonable cost, would pay extra for the reference and selection of appropriate paper stock, but this isn't required.

Don't hesitate if you need additional info for your design. Will provide detailed text to the contest winner.

```html
<!DOCTYPE html>
<html lang="en">
<head>
<meta charset="utf-8">
<title>Tobias Wenkle – Business Card</title>
<link rel="stylesheet" href="https://fonts.googleapis.com/css2?family=Open+Sans:wght@400;600;700&display=swap">
<style>
  :root {
    --page-bg: #e6e6e6;
    --card-bg: #ffffff;
    --band-bg: #333333;
    --accent-blue: #4a6bc4;
    --ink: #1f1f1f;
    --band-text: #f4f4f4;
    --divider: #2a2a2a;
  }
  * { box-sizing: border-box; margin: 0; padding: 0; }
  html, body {
    width: 1200px; height: 944px; overflow: hidden;
    background: var(--page-bg);
    font-family: "Open Sans", Arial, sans-serif;
  }
  .card {
    position: absolute; left: 100px; top: 186px;
    width: 1000px; height: 572px;
    background: var(--card-bg);
    box-shadow: 0 6px 18px rgba(0,0,0,0.18);
    overflow: hidden;
  }
  .brand {
    position: absolute; left: 70px; top: 215px; width: 260px;
    display: flex; align-items: center; gap: 12px;
    color: var(--accent-blue); font-weight: 700; font-size: 22px;
    letter-spacing: 1px;
  }
  .brand-square {
    width: 22px; height: 22px; background: var(--accent-blue); flex: none;
  }
  .divider {
    position: absolute; left: 372px; top: 160px;
    width: 2px; height: 250px; background: var(--divider);
  }
  .identity {
    position: absolute; right: 58px; top: 62px; text-align: right;
  }
  .identity-name {
    color: var(--accent-blue); font-weight: 700; font-size: 40px;
    letter-spacing: 5px; line-height: 1.1;
  }
  .identity-role {
    color: var(--ink); font-weight: 600; font-size: 15px;
    letter-spacing: 2.5px; margin-top: 2px;
  }
  .contacts {
    position: absolute; left: 410px; top: 228px; list-style: none;
  }
  .contact {
    display: flex; align-items: center; gap: 16px;
    font-size: 19px; letter-spacing: 2.5px; color: var(--ink);
    height: 42px;
  }
  .contact-icon { width: 22px; height: 22px; flex: none; }
  .website {
    position: absolute; left: 400px; top: 378px;
    font-size: 24px; letter-spacing: 3.5px; color: var(--ink);
  }
  .website strong { font-weight: 700; }
  .address-band {
    position: absolute; left: 0; bottom: 0; width: 100%; height: 118px;
    background: var(--band-bg);
    display: flex; align-items: center; padding-left: 80px;
    color: var(--band-text); font-weight: 600; font-size: 19px;
    letter-spacing: 3px;
  }
</style>
</head>
<body>
  <article class="card">
    <div class="brand"><span class="brand-square"></span>Wenkle Advisory</div>
    <div class="divider"></div>

    <header class="identity">
      <h1 class="identity-name">TOBIAS WENKLE</h1>
      <p class="identity-role">MICROFINANCE CONSULTANT</p>
    </header>

    <ul class="contacts">
      <li class="contact">
        <svg class="contact-icon" viewBox="0 0 24 24" aria-hidden="true">
          <path fill="#4a6bc4" d="M6.6 10.8a15.1 15.1 0 0 0 6.6 6.6l2.2-2.2c.3-.3.7-.4 1-.2 1.1.4 2.3.6 3.6.6.6 0 1 .4 1 1V20c0 .6-.4 1-1 1C10.6 21 3 13.4 3 4c0-.6.4-1 1-1h3.5c.6 0 1 .4 1 1 0 1.3.2 2.5.6 3.6.1.3 0 .7-.2 1z"/>
        </svg>
        +32 470 512 84
      </li>
      <li class="contact">
        <svg class="contact-icon" viewBox="0 0 24 24" aria-hidden="true">
          <rect x="2" y="5" width="20" height="14" fill="#4a6bc4"/>
          <path d="M2.5 5.5 12 13l9.5-7.5" fill="none" stroke="#fff" stroke-width="1.6"/>
        </svg>
        tobias@tobiaswenkle.com
      </li>
      <li class="contact">
        <svg class="contact-icon" viewBox="0 0 24 24" aria-hidden="true">
          <circle cx="12" cy="12" r="10" fill="#4a6bc4"/>
        </svg>
        TOBIASWENKLE
      </li>
    </ul>

    <p class="website">WWW.<strong>TOBIASWENKLE</strong>.COM</p>

    <footer class="address-band">1480 LINDEN HOLLOW ROAD, B2K 4M7 VERDALE</footer>
  </article>
</body>
</html>
```